Set of 6 Icons and buttons required

We have written a windows based app which gives clients access to reports etc.

We are a multichannel epos company

We require 6 buttons and icons along with a suggested font to use and a background for the form.

I have attatched a mock up of what we require from the chosen designer.

The buttons are as follows :

Stockcard ( This is a program which customers can enter stock and check stock levels etc )

Reports ( as the title says )

Stock ( This for making adjustments )

Goods ( this is for booking goods in )

Settings ( As title says )

Help ( As title says )

Dimensions
---------------

The form : 296x268
Buttons : 218x36
Icons on button : 32x32
Text size : Size 10

If you look at the attatched document this is something I put together just to show what we are looking once we put all the components together

Our website is q-ledgora.co.uk

Target Market(s)

B2B

Industry/Entity Type

It Company

```html
<!DOCTYPE html>
<html lang="en">
<head>
<meta charset="utf-8">
<title>q-ledgora launcher</title>
<link rel="stylesheet" href="https://fonts.googleapis.com/css2?family=Noto+Sans:wght@400;700&display=swap">
<style>
  :root {
    --bg-top: #0f2966;
    --bg-bottom: #4c74c6;
    --panel: #2b2e39;
    --panel-edge: #3b3f4c;
    --btn-top: #2e2e30;
    --btn-bottom: #151516;
    --btn-edge: #4a4a4e;
    --btn-text: #f4f4f4;
    --active-top: #f7f7f7;
    --active-bottom: #c9c9c9;
    --active-text: #5a5a5a;
    --brand-text: #e9ecf3;
    --brand-mark: #2f7fd0;
    --close: #d6d6d6;
  }
  * { box-sizing: border-box; margin: 0; padding: 0; }
  html, body { width: 1200px; height: 1117px; overflow: hidden; }
  body {
    position: relative;
    background: linear-gradient(180deg, var(--bg-top) 0%, var(--bg-bottom) 100%);
    font-family: "Noto Sans", Tahoma, sans-serif;
  }
  .launcher {
    position: absolute;
    left: 339px; top: 323px;
    width: 522px; height: 471px;
    background: var(--panel);
    border: 2px solid var(--panel-edge);
  }
  .launcher__close {
    position: absolute;
    right: 14px; top: 10px;
    width: 24px; height: 24px;
  }
  .brand {
    position: absolute;
    left: 56px; top: 266px;
    transform: translate(-50%, -50%) rotate(-90deg);
    white-space: nowrap;
    font-weight: 400;
    font-size: 46px;
    letter-spacing: 1px;
    color: var(--brand-text);
  }
  .brand__mark {
    position: absolute;
    left: 18px; top: 373px;
    width: 76px; height: 76px;
    background: var(--brand-mark);
  }
  .menu {
    position: absolute;
    left: 118px; top: 45px;
    width: 395px;
    list-style: none;
  }
  .menu__item {
    display: flex;
    align-items: center;
    height: 65px;
    margin-bottom: 4px;
    padding-left: 14px;
    background: linear-gradient(180deg, var(--btn-top), var(--btn-bottom));
    border: 2px solid var(--btn-edge);
    color: var(--btn-text);
    font-weight: 700;
    font-size: 24px;
    letter-spacing: 0.5px;
  }
  .menu__item--active {
    background: linear-gradient(180deg, var(--active-top), var(--active-bottom));
    border-color: #e6e6e6;
    color: var(--active-text);
  }
  .menu__icon {
    width: 38px; height: 38px;
    margin-right: 20px;
    flex: none;
  }
</style>
</head>
<body>
  <section class="launcher">
    <svg class="launcher__close" viewBox="0 0 24 24" aria-label="Close">
      <path d="M4 4 L20 20 M20 4 L4 20" stroke="var(--close)" stroke-width="4.5" stroke-linecap="round"/>
    </svg>

    <div class="brand">q-ledgora</div>
    <div class="brand__mark"></div>

    <ul class="menu">
      <li class="menu__item">
        <svg class="menu__icon" viewBox="0 0 38 38">
          <rect x="3" y="3" width="32" height="32" fill="none" stroke="#f0f0f0" stroke-width="3"/>
          <rect x="3" y="3" width="32" height="6" fill="#f0f0f0"/>
          <path d="M8 15H30M8 20H30M8 25H30M8 30H30" stroke="#f0f0f0" stroke-width="2"/>
        </svg>
        Stockcard
      </li>
      <li class="menu__item menu__item--active">
        <svg class="menu__icon" viewBox="0 0 38 38">
          <circle cx="19" cy="19" r="16" fill="#5a5a5a"/>
          <path d="M19 19 L19 3 A16 16 0 0 1 34 14 Z" fill="#d8d8d8"/>
        </svg>
        Reports
      </li>
      <li class="menu__item">
        <svg class="menu__icon" viewBox="0 0 38 38">
          <path d="M2 24 L9 16 L15 23 L22 15 L28 22 L36 14" fill="none" stroke="#e8e8e8" stroke-width="3" stroke-linejoin="round"/>
        </svg>
        Stock
      </li>
      <li class="menu__item">
        <svg class="menu__icon" viewBox="0 0 38 38" fill="#e0e0e0">
          <rect x="16" y="5" width="10" height="9"/>
          <rect x="4" y="16" width="10" height="9"/>
          <rect x="16" y="16" width="10" height="9"/>
          <rect x="4" y="27" width="10" height="9"/>
          <rect x="16" y="27" width="10" height="9"/>
          <rect x="28" y="27" width="8" height="9"/>
        </svg>
        Goods
      </li>
      <li class="menu__item">
        <svg class="menu__icon" viewBox="0 0 38 38">
          <circle cx="19" cy="19" r="14" fill="none" stroke="#e8e8e8" stroke-width="7" stroke-dasharray="5.5 5.5"/>
          <circle cx="19" cy="19" r="10" fill="#e8e8e8"/>
          <circle cx="19" cy="19" r="4.5" fill="#1f1f20"/>
        </svg>
        Settings
      </li>
      <li class="menu__item">
        <svg class="menu__icon" viewBox="0 0 38 38">
          <path d="M12 12 Q12 5 19 5 Q26 5 26 12 Q26 16 21 19 Q19 21 19 25" fill="none" stroke="#e8e8e8" stroke-width="4.5" stroke-linecap="round"/>
          <circle cx="19" cy="33" r="3" fill="#e8e8e8"/>
        </svg>
        Help
      </li>
    </ul>
  </section>
</body>
</html>
```